Business Card - connecting 2 souls and beggining the journey of self discovery

Logo on the front
with tag line

On the back list of services and contact details

Seminars
workshops
Coaching
podcasts

Daniel Porthwick
Health & Wellbeing Life Coach
0491 372 815
daniel@wovenpathwellness.example
wovenpathwellness.example

Industry/Entity Type

Life Coaching

Contact Information for Business Card

I like the use of colour from the logo to be used. I'm not a fan of white.

Requirements
Must have
• My tagline: The journey home starts with you
Nice to have
• Use of colour that is in the mind body soul logo

```html
<!DOCTYPE html>
<html lang="en">
<head>
<meta charset="utf-8">
<title>Woven Path Wellness – Business Card</title>
<link href="https://fonts.googleapis.com/css2?family=Montserrat:wght@300;400;500&display=swap" rel="stylesheet">
<style>
  :root {
    --page: #ffffff;
    --sun: #f6c419;
    --sun-deep: #eeb413;
    --plum: #6a2d8f;
    --slate: #6f6f72;
    --slate-dark: #4a4a4e;
    --ink-grey: #5d5d60;
    --white: #ffffff;
    --band: rgba(80, 80, 84, 0.55);
  }
  * { margin: 0; padding: 0; box-sizing: border-box; }
  html, body { width: 800px; height: 1200px; overflow: hidden; background: var(--page); }
  body { position: relative; font-family: "Montserrat", Arial, sans-serif; }

  /* Front side */
  .card-front { position: absolute; left: 0; top: 0; width: 800px; height: 480px; }
  .brand-mark {
    position: absolute; left: 314px; top: 108px; width: 172px; height: 172px;
    border-radius: 50%;
    background: radial-gradient(circle at 40% 40%, #f39a1e 0%, #e8447a 45%, #6a2d8f 80%);
  }
  .brand-name {
    position: absolute; left: 0; width: 800px; top: 314px;
    text-align: center; font-weight: 300; font-size: 40px; line-height: 48px; color: var(--ink-grey);
    letter-spacing: -0.3px; white-space: nowrap;
  }
  .tag-shape { position: absolute; left: 21px; top: 370px; width: 758px; height: 110px; }
  .tagline {
    position: absolute; left: 0; width: 800px; top: 380px;
    text-align: center; font-weight: 400; font-size: 25px; line-height: 34px; color: var(--plum);
    white-space: nowrap;
  }

  /* Back side */
  .card-back { position: absolute; left: 21px; top: 672px; width: 758px; height: 450px; overflow: hidden; }
  .back-stripe-top { position: absolute; left: 0; top: 0; width: 758px; height: 22px; background: var(--sun); }
  .back-photo {
    position: absolute; left: 0; top: 22px; width: 758px; height: 372px;
    background:
      radial-gradient(ellipse 230px 260px at 310px 200px, rgba(246,196,25,0.85), rgba(246,196,25,0) 70%),
      linear-gradient(135deg, #9a9a9c 0%, var(--slate) 45%, var(--slate-dark) 100%);
  }
  .name-band { position: absolute; left: 0; top: 42px; width: 758px; height: 60px; background: var(--band); }
  .holder-name {
    position: absolute; left: 12px; top: 51px;
    font-weight: 400; font-size: 33px; line-height: 42px; color: var(--white);
    text-transform: uppercase; letter-spacing: 0.3px; white-space: nowrap;
  }
  .holder-role {
    position: absolute; right: 12px; top: 60px;
    font-size: 18px; line-height: 24px; color: var(--white); white-space: nowrap;
  }
  .services { position: absolute; left: 100px; top: 164px; width: 200px; list-style: none; text-align: right; }
  .services li { font-size: 19px; color: var(--slate-dark); line-height: 33px; }
  .services li:nth-child(2) { padding-right: 20px; }
  .services li:nth-child(3) { padding-right: 40px; }
  .services li:nth-child(4) { padding-right: 60px; }
  .contact { position: absolute; right: 20px; top: 256px; text-align: right; list-style: none; }
  .contact li { font-size: 19px; color: var(--white); line-height: 32px; white-space: nowrap; }
  .back-stripe-bottom { position: absolute; left: 0; top: 394px; width: 758px; height: 22px; background: var(--sun); }
  .back-foot { position: absolute; left: 0; top: 416px; width: 758px; height: 34px; background: var(--slate); }
</style>
</head>
<body>
  <section class="card-front">
    <div class="brand-mark"></div>
    <h1 class="brand-name">Woven Path Wellness</h1>
    <svg class="tag-shape" viewBox="0 0 758 110" aria-hidden="true">
      <path d="M0 58 H88 V18 Q88 2 106 2 H652 Q670 2 670 18 V58 H758 V110 H0 Z" fill="var(--sun)"/>
      <path d="M0 58 H758" stroke="var(--sun-deep)" stroke-width="2"/>
    </svg>
    <p class="tagline">The journey home starts with you</p>
  </section>

  <section class="card-back">
    <div class="back-stripe-top"></div>
    <div class="back-photo" role="img" aria-label="Abstract photographic backdrop in warm yellow and grey tones"></div>
    <div class="name-band"></div>
    <h2 class="holder-name">Daniel Porthwick</h2>
    <p class="holder-role">Health &amp; Wellbeing Life Coach</p>
    <ul class="services">
      <li>Seminars</li>
      <li>Workshops</li>
      <li>Coaching</li>
      <li>Podcasts</li>
    </ul>
    <ul class="contact">
      <li>214 Larkspur Lane, Portland 97205</li>
      <li>0491 372 815</li>
      <li>daniel@wovenpathwellness.example</li>
      <li>wovenpathwellness.example</li>
    </ul>
    <div class="back-stripe-bottom"></div>
    <div class="back-foot"></div>
  </section>
</body>
</html>
```